Sports Psychology Business Card Design

Need a catchy and unique business card design for our sport psychology practice. We provide mental performance counseling and consulting to performers from all types of industries with a special emphases on athletes.The name of our practice is "Inner Edge of Excellence" or "IEE" as is indicated in the logo examples submitted in this brief. Also provided were logos with specific sports referenced which represent sources of our clients from those sports.

Target Market(s)

Executives, Professionals (doctors, lawyers, etc.), Athletes, Entertainers and other performers

Contact Information for Business Card

Need to include our logo (logos provided in this brief).

Font styles to use
Other font styles liked:
• Font can be found in logo

Colors
0792cd
34a7d8
85cae6

Requirements
Must have
• Our logo and reference to our provision of mental performance counseling/consulting/coaching
Nice to have
• References to sports that our athletes play as provided in the brief.
Should not have
• This is not a general wellness consulting practice. Our focus is on consulting to improve mental performance.

```html
<!DOCTYPE html>
<html lang="en">
<head>
<meta charset="UTF-8">
<title>Daniel Whitcombe – Business Card</title>
<link href="https://fonts.googleapis.com/css2?family=Open+Sans:wght@400;600;700&family=Cutive&display=swap" rel="stylesheet">
<style>
  :root {
    --ink: #000000;
    --paper: #ffffff;
    --accent: #0792cd;
    --accent-mid: #34a7d8;
    --accent-light: #85cae6;
    --rail: #c8c8c8;
    --text-dark: #111111;
  }
  html, body {
    margin: 0;
    padding: 0;
    width: 1200px;
    height: 721px;
    overflow: hidden;
    background: var(--paper);
  }
  .card {
    position: relative;
    width: 1200px;
    height: 721px;
    box-sizing: border-box;
    border: 2px solid var(--ink);
    background: var(--paper);
    overflow: hidden;
    font-family: "Open Sans", Arial, sans-serif;
  }
  .card__frame {
    position: absolute;
    inset: 0;
  }
  .card__name {
    position: absolute;
    top: 82px;
    left: 0;
    width: 1165px;
    margin: 0;
    text-align: center;
    font-size: 41px;
    font-weight: 400;
    color: var(--text-dark);
  }
  .card__name strong { font-weight: 700; }
  .brand {
    position: absolute;
    top: 182px;
    left: 0;
    width: 1200px;
    height: 228px;
    display: flex;
    align-items: center;
    justify-content: center;
  }
  .brand__name {
    font-family: "Open Sans", Arial, sans-serif;
    font-weight: 700;
    font-size: 170px;
    line-height: 1;
    letter-spacing: 6px;
    color: var(--accent);
  }
  .tagline {
    position: absolute;
    top: 425px;
    left: 0;
    width: 1200px;
    margin: 0;
    text-align: center;
    font-family: "Cutive", "Courier New", serif;
    font-size: 37px;
    line-height: 1.2;
    color: var(--ink);
  }
  .services {
    position: absolute;
    top: 492px;
    left: 0;
    width: 1200px;
    margin: 0;
    text-align: center;
    font-size: 19px;
    font-weight: 600;
    letter-spacing: 2px;
    text-transform: uppercase;
    color: var(--accent);
  }
  .contact {
    position: absolute;
    left: 0;
    width: 1200px;
    display: flex;
    justify-content: center;
    align-items: center;
    color: var(--paper);
  }
  .contact--address {
    top: 590px;
    font-size: 21px;
    font-weight: 400;
  }
  .contact--lines {
    top: 638px;
    font-size: 23px;
    font-weight: 700;
    gap: 24px;
  }
  .contact__item {
    display: flex;
    align-items: center;
    gap: 8px;
  }
  .contact__icon {
    fill: var(--accent-light);
    flex: none;
  }
</style>
</head>
<body>
<div class="card">
  <svg class="card__frame" width="1200" height="721" viewBox="0 0 1200 721" aria-hidden="true">
    <rect class="rail" x="1165" y="0" width="35" height="721" fill="var(--rail)"/>
    <polygon class="band-top" points="0,0 1113,0 1094,34 0,34" fill="var(--ink)"/>
    <polygon class="band-bottom" points="0,564 1165,564 1165,612 1113,721 0,721" fill="var(--ink)"/>
    <rect class="band-bottom__edge" x="0" y="564" width="1165" height="4" fill="var(--accent-mid)"/>
  </svg>

  <h1 class="card__name"><strong>Daniel</strong> Whitcombe</h1>

  <div class="brand">
    <span class="brand__name">IEE</span>
  </div>

  <p class="tagline">The Inner Edge Of Excellence</p>
  <p class="services">Mental Performance Counseling &amp; Consulting</p>

  <div class="contact contact--address">
    <span class="contact__item">
      <svg class="contact__icon" width="16" height="22" viewBox="0 0 16 22" aria-hidden="true">
        <path d="M8 0C3.6 0 0 3.5 0 7.9 0 13.6 8 22 8 22s8-8.4 8-14.1C16 3.5 12.4 0 8 0zm0 11a3 3 0 1 1 0-6 3 3 0 0 1 0 6z"/>
      </svg>
      1200 Harbor Lane, Suite 300, Bay Street,
    </span>
  </div>

  <div class="contact contact--lines">
    <span class="contact__item">
      <svg class="contact__icon" width="30" height="22" viewBox="0 0 30 22" aria-hidden="true">
        <path d="M2 6C2 2 8 1 15 1s13 1 13 5v2h-7V5c-2-.6-4-.8-6-.8S11 4.4 9 5v3H2z"/>
        <path d="M8 9h14l4 12H4z"/>
        <rect x="11" y="12" width="8" height="6" fill="var(--ink)"/>
      </svg>
      +858-555-0147
    </span>
    <span class="contact__item">
      <svg class="contact__icon" width="30" height="22" viewBox="0 0 30 22" aria-hidden="true">
        <path d="M1 1h28v20H1z M3.5 3v.3L15 12.5 26.5 3.3V3z M3 5.8V19h24V5.8L15 15.2z" fill-rule="evenodd"/>
      </svg>
      Email:daniel@theiee.co
    </span>
    <span class="contact__item">
      <svg class="contact__icon" width="26" height="26" viewBox="0 0 26 26" aria-hidden="true">
        <g fill="none" stroke="var(--accent-light)" stroke-width="2">
          <circle cx="13" cy="13" r="11.5"/>
          <ellipse cx="13" cy="13" rx="5" ry="11.5"/>
          <line x1="1.5" y1="13" x2="24.5" y2="13"/>
          <path d="M3.5 7h19M3.5 19h19"/>
        </g>
      </svg>
      www.theiee.com
    </span>
  </div>
</div>
</body>
</html>
```